Flyer-Design für Pädagogisch-Psychologische Beratung
Zielgruppe
Mein Unternehmen heißt 'velunado Pädagogisch-Psychologische Beratung'. velunado ist lateinisch für begleiten. Mein Name ist Ortwin Stalbrech, ich bin Pädagoge und Psychologe
Meine Zielgruppe sind
-Eltern (Seminare zu den Bedürfnissen eines Kindes, Bindungs- und Erziehungsberatung)
-pädagogische Fachkräfte (Beratung von Einzelpersonen und Teams in Bindungs und Erziehungsfragen als auch zu Teamprozessen)
-Gerichte (Erstellung familienpsychologischer Gutachten)
My company is called 'velunado educational-psychological consulting'. velunado is Latin for accompany. My name is Ortwin Stalbrech, I am an educator and psychologist.
My target groups are
-Parents (seminars on the needs of a child, bonding and educational counseling)
-educational professionals (counseling individuals and teams on attachment and parenting issues as well as team processes)
-courts (preparation of family psychological reports)
Aufgabenstellung
Ich hätte gerne einen Flyer (DIN lang, 6 seitig, Maße siehe 'Vorlage Flyer' bei den Dateien), für mein Elternseminar.
Ich möchte einen Flyer, der ein schönes farbliches Konzept hat: professionell aber nicht zu ernst, freundlich-offen aber nicht kitschig.
Das Design soll dann später für Flyer für meine anderen Angebote genutzt werden (als Folgeauftrag/ 1:1 Projekt), dann aber als 4 seitiger Flyer ohne Anmeldeformular.
Text und Inhalte für den Flyer sind im PDF 'Flyer_Inhalte_und_Text'. Alles in ROT sind Hinweise und sollen nicht Teil des Flyers sein.
Ich bin aber offen für Vorschläge z.B. für eine andere Aufteilung der Inhalte.
Ich bin mir nicht sicher, ob ich Stock-Fotos auf dem Flyer haben möchte, aber ich habe mal Beispiele mit hochgeladen, die ich mir vorstellen könnte ('baby' und 'parents'). Es steht den Designern aber auch frei, eigene Stock-Fotos einzufügen, die ich dann erwerben würde.
Von den Farben sollte es sich an dem Grün (R:54 G:197 B:144 (#36C590)) und dem Orange (R:255 G:161 B:2 (#FFA102)) aus dem Logo orientieren.
Die Schriftarten vom Logo sind 'Aller Bold' (Name) und Engravers Gothic BT (Untertitel).
I would like to have a flyer (DIN long, 6 pages, dimensions see 'Template Flyer' at the files), for my parent seminar.
I would like a flyer that has a nice color concept: professional but not too serious, friendly-open but not kitschy.
The design is to be used later for flyers for my other offers (as a follow-up order/ 1:1 project), but then as a 4-page flyer without a registration form.
Text and content for the flyer are in the PDF 'Flyer_Content_and_Text'. Everything in RED are hints and should not be part of the flyer.
However, I am open to suggestions e.g. for a different division of the content.
I'm not sure I want stock photos on the flyer, but I've uploaded examples I could imagine ('baby' and 'parents'). However, designers are also free to add the..

```html
<!DOCTYPE html>
<html lang="de">
<head>
<meta charset="utf-8">
<title>velunado – Elternseminar NAH+SICHER</title>
<link href="https://fonts.googleapis.com/css2?family=Fira+Sans:ital,wght@0,400;1,400&family=Syncopate&display=swap" rel="stylesheet">
<style>
  :root{
    --orange:#FFA102;
    --green:#4DB78C;
    --ink:#1f1f1f;
    --rule:#9a9a9a;
    --shade:#efefef;
    --paper:#ffffff;
  }
  *{margin:0;padding:0;box-sizing:border-box}
  html,body{width:1200px;height:818px;overflow:hidden;background:var(--paper)}
  .flyer{position:relative;width:1200px;height:818px;overflow:hidden;
    font-family:"Fira Sans",Arial,sans-serif;color:var(--ink)}
  .shapes{position:absolute;inset:0}
  .fold{position:absolute;top:0;width:1px;height:818px;background:var(--rule)}
  .heading{position:absolute;font-family:"Syncopate",Arial,sans-serif;font-weight:400;
    color:var(--orange);font-size:16.5px;letter-spacing:.3px;line-height:1;white-space:nowrap}
  .underline{position:absolute;height:1.5px;background:var(--orange)}
  .text{position:absolute;font-size:12px;line-height:16.3px;white-space:nowrap}
  .text p{margin:0}
  .accent{color:var(--green);font-style:italic}
  .list{list-style:none}
  .list li{padding-left:9px;text-indent:-9px;margin-bottom:4px}
  .list li::before{content:"- "}
  .dates div{height:20.3px}
  .small{font-size:10.6px;line-height:12.3px}
  .form-line{position:absolute;left:829px;width:323px;height:1px;background:#555}
  .form-label{position:absolute;left:831px;font-size:10.8px;white-space:nowrap}
  .form-label small{font-size:7.6px}
  .option{position:absolute;left:828px;font-size:12.2px;display:flex;align-items:center;gap:7px;white-space:nowrap}
  .option i{display:inline-block;width:11px;height:11px;border:1px solid #333;border-radius:50%}
  .note{position:absolute;font-size:7.8px;line-height:10px;white-space:nowrap}
</style>
</head>
<body>
<div class="flyer">

  <svg class="shapes" width="1200" height="818" viewBox="0 0 1200 818">
    <defs>
      <linearGradient id="parentsTone" x1="0" y1="0" x2="1" y2="1">
        <stop offset="0" stop-color="#3b4a3a"/>
        <stop offset=".45" stop-color="#7aa34c"/>
        <stop offset=".75" stop-color="#c9a58a"/>
        <stop offset="1" stop-color="#4a3a2c"/>
      </linearGradient>
      <linearGradient id="hugTone" x1="0" y1="0" x2="1" y2="1">
        <stop offset="0" stop-color="#f2d3b0"/>
        <stop offset=".5" stop-color="#c99a72"/>
        <stop offset="1" stop-color="#e9e4dd"/>
      </linearGradient>
    </defs>
    <circle cx="82" cy="-2" r="110" fill="var(--orange)"/>
    <circle cx="44" cy="103" r="31" fill="var(--green)"/>
    <path d="M527,0 L708,0 C712,40 700,75 678,95 C665,105 650,96 638,85 C610,60 585,35 550,25 C530,18 525,8 527,0 Z" fill="var(--green)"/>
    <path d="M695,0 L1200,0 L1200,160 C1150,222 1100,222 1060,212 C950,218 880,168 796,66 C776,36 738,12 695,0 Z" fill="var(--shade)"/>
    <path d="M702,0 L1200,0 L1200,150 C1150,212 1100,214 1060,205 C955,210 885,160 803,58 C783,30 745,8 702,0 Z" fill="var(--orange)"/>
    <circle cx="1105" cy="187" r="77" fill="url(#hugTone)" role="img" aria-label="Foto: Vater hält sein Kind liebevoll im Arm"/>
    <path d="M132,672 C135,655 150,654 180,655 C260,655 320,630 400,606 C440,597 455,640 453,690 C450,740 420,790 372,818 L192,818 C160,780 128,720 132,672 Z" fill="url(#parentsTone)" role="img" aria-label="Foto: Elternpaar hält kleine Babyschuhe in der Hand"/>
    <circle cx="444" cy="624" r="31" fill="var(--green)"/>
  </svg>

  <div class="fold" style="left:401px"></div>
  <div class="fold" style="left:802px"></div>

  <!-- Panel 1 -->
  <h2 class="heading" style="left:174px;top:104px">WARUM NAH+SICHER?</h2>
  <div class="underline" style="left:175px;top:123px;width:226px"></div>

  <div class="text" style="left:22px;top:147px">
    <p>Weil ein Kind Nähe und Sicherheit benötigt, damit es sich gut<br>entwickeln kann. Nur dann bekommt das Kind eine gute<br>Grundlage für die Herausforderungen seines Menschenlebens.</p>
  </div>
  <div class="text" style="left:22px;top:212px">
    <p>Daneben dann noch die Vorbereitung auf die ersten Lebens-<br>monate des Säuglings. Sollte ich mein Kind stillen und wenn ja,<br>wie lange? Was benötige ich an Kleidung für das Neugeborene?<br>Eventuell soll auch noch ein Kinderzimmer renoviert und mit<br>Möbeln ausgestattet werden. Das ist auch alles richtig und wichtig.<br>Oft wird aber an die Vorbereitung auf einen anderen, wichtigen<br>Punkt nicht gedacht: <span class="accent">Wie sich durch die Geburt eines Kindes auch<br>der Alltag der Eltern verändert.</span></p>
  </div>
  <ul class="text list" style="left:22px;top:373px">
    <li>Wie lebt man als Familie, so dass die Bedürfnisse<br>des Kindes erfüllt werden, die Bedürfnisse der<br>Eltern aber nicht vernachlässigt werden?</li>
    <li>Müssen die Rollen innerhalb der Partnerschaft eventuell<br>neu verteilt werden? Wie wird die Versorgung des Kindes<br>und die Berufstätigkeit miteinander vereinbart?</li>
    <li>Wie entwickelt sich ein Kind gut, wie wächst es NAH+SICHER auf?</li>
  </ul>
  <div class="text" style="left:22px;top:527px">
    <p>Das Seminar soll Ihnen dabei helfen, dass Sie ihrer Familie schon<br>vorher eine gute Struktur geben können. Es wird Raum für die<br>Fragen der Eltern geben und die Möglichkeit, sich mit den eigenen<br>Erfahrungen und Vorstellungen auseinanderzusetzen.</p>
  </div>

  <!-- Panel 2 -->
  <h2 class="heading" style="left:429px;top:104px">INHALTE</h2>
  <div class="underline" style="left:401px;top:123px;width:98px"></div>
  <ul class="text list" style="left:422px;top:146px">
    <li>Einführung in die Bindungstheorie: Eine sichere Basis für eine<br>gute Entwicklung.</li>
    <li>Die Bedürfnisse eines Kindes: Was braucht ein Kind zu<br>welcher Zeit? Auseinandersetzung mit den wichtigsten<br>Entwicklungsbereichen.</li>
    <li>Was bedeutet Erziehung: Auseinandersetzung mit verschiedenen<br>Erziehungsmodellen und den eigenen Erfahrungen.</li>
    <li>Elternschaft, Partnerschaft, Selbsterfüllung: Wie können<br>diese Bereiche gut miteinander vereinbart werden?</li>
    <li>Vorstellung von Beratungs- und Hilfsangeboten: An welche Stelle<br>kann ich mich wenden, wenn ich Beratung oder Hilfe benötige?</li>
  </ul>

  <h2 class="heading" style="left:429px;top:367px">TERMINE</h2>
  <div class="underline" style="left:402px;top:386px;width:104px"></div>
  <div class="text dates" style="left:430px;top:390px">
    <div>Seminar 1: 11.05. bis 22.06.2022, jeden MI 19-21 Uhr</div>
    <div>Seminar 2: 14.05. bis 15.05.2022, SA 10-18 Uhr, SO 10-16 Uhr</div>
    <div>Seminar 3: 25.06. bis 26.06.2022, SA 10-18 Uhr, SO 10-16 Uhr</div>
  </div>

  <h2 class="heading" style="left:431px;top:475px">PREIS</h2>
  <div class="underline" style="left:402px;top:494px;width:82px"></div>
  <div class="text" style="left:431px;top:499px">Pro Elternteil 175 € / Pro Elternpaar 300 €</div>
  <div class="text small" style="left:431px;top:521px">Sollte Ihnen die Finanzierung des Teilnahmepreises nicht möglich sein,<br>kann evtl. eine Unterstützung durch dritte Stellen ermöglicht werden.<br>Schreiben Sie dazu bitte eine Nachricht an o.stalbrech@velunado.de.</div>

  <h2 class="heading" style="left:502px;top:590px">ORT</h2>
  <div class="underline" style="left:485px;top:609px;width:50px"></div>
  <div class="text" style="left:502px;top:614px;line-height:15px">Jugendhaus Lindenhain,<br>Birkenweg 12, 32400 Musterstadt</div>
  <div class="text accent" style="left:502px;top:679px;line-height:14.8px">Weitere Informationen zum Seminar und aktuelle<br>Entwicklungen aufgrund der Corona-Pandemie<br>finden Sie unter www.velunado.de</div>

  <!-- Panel 3 -->
  <h2 class="heading" style="left:828px;top:238px">ANMELDEFORMULAR</h2>
  <div class="underline" style="left:803px;top:257px;width:206px"></div>

  <div class="form-line" style="top:288px"></div><div class="form-label" style="top:290px">Name</div>
  <div class="form-line" style="top:323px"></div><div class="form-label" style="top:326px">evtl. Name weiterer Elternteil</div>
  <div class="form-line" style="top:358px"></div><div class="form-label" style="top:360px">(voraussichtliches) Geburtsdatum des Kindes</div>
  <div class="form-line" style="top:393px"></div><div class="form-label" style="top:394px">Straße und Hausnummer</div>
  <div class="form-line" style="top:428px"></div><div class="form-label" style="top:431px">Postleitzahl und Ort</div>
  <div class="form-line" style="top:463px"></div><div class="form-label" style="top:465px">Telefonnummer</div>
  <div class="form-line" style="top:497px"></div><div class="form-label" style="top:500px">E-Mail Adresse <small>(hierüber werden Ihnen alle weiteren Informationen zugestellt)</small></div>

  <h2 class="heading" style="left:833px;top:538px">WAHL DES SEMINARS</h2>
  <div class="option" style="top:559px"><i></i>Seminar 1: 11.05. bis 22.06.2022</div>
  <div class="option" style="top:579px"><i></i>Seminar 2: 14.05. bis 15.05.2022</div>
  <div class="option" style="top:599px"><i></i>Seminar 3: 25.06. bis 26.06.2022</div>

  <div class="form-line" style="top:659px;width:288px"></div>
  <div class="form-label" style="top:667px;left:846px">Datum</div>
  <div class="form-label" style="top:667px;left:1040px">Unterschrift</div>
  <div class="note" style="left:829px;top:693px">Mit meiner Unterschrift erkläre ich mein Einverständnis mit den Allgemeinen<br>Geschäftsbedingungen (AGB) und Datenschutzbedingungen (siehe www.velunado.de).</div>
  <div class="text small" style="left:828px;top:737px;font-size:11px;line-height:13.3px">Nach Eingang des Formulars erhalten Sie per E-Mail eine<br>Anmeldebestätigung, die Zahlungsanweisungen und weitere<br>Informationen zum Ablauf des Seminars.</div>

</div>
</body>
</html>
```